Business Card Design

We are a commercial real estate brokerage in San Francisco, leasing office buildings downtown.
I would like a clean, elegant look. Simple but powerful .

Industry/Entity Type

Business

Contact Information for Business Card

Colin Farrow
lic# 07281549
415.555.0172
colin@tarvo-commercial.example
tarvo-commercial.example

```html
<!DOCTYPE html>
<html lang="en">
<head>
<meta charset="utf-8">
<title>Tarvo Commercial — Business Card</title>
<link rel="stylesheet" href="https://fonts.googleapis.com/css2?family=PT+Sans:wght@400;700&display=swap">
<style>
  :root {
    --backdrop: #929292;
    --card: #eaeaed;
    --brand-blue: #5d7196;
    --ink: #3f3f42;
    --rule: #2f2f32;
    --mark: #4a4a4e;
    --skyline-top: rgba(150, 150, 160, 0.22);
    --skyline-bottom: rgba(150, 150, 160, 0.12);
  }
  * { box-sizing: border-box; margin: 0; padding: 0; }
  html, body { width: 1105px; height: 1200px; overflow: hidden; }
  body {
    background: var(--backdrop);
    font-family: "PT Sans", Arial, sans-serif;
    position: relative;
  }
  .card {
    position: absolute;
    left: 182px;
    width: 746px;
    height: 426px;
    background: var(--card);
    overflow: hidden;
  }
  .card--front { top: 120px; }
  .card--back { top: 637px; }

  .skyline-backdrop {
    position: absolute;
    right: 0;
    top: 0;
    width: 330px;
    height: 426px;
    background: linear-gradient(180deg, var(--skyline-top), var(--skyline-bottom));
  }

  .brand {
    position: absolute;
    display: flex;
    align-items: center;
  }
  .brand__square {
    width: 96px;
    height: 78px;
    background: var(--mark);
  }
  .brand__rule {
    width: 2px;
    background: var(--rule);
  }
  .brand__name {
    color: var(--brand-blue);
    font-weight: 700;
    line-height: 0.95;
    text-transform: uppercase;
  }
  .brand__name span { display: block; }

  /* front */
  .card--front .brand { left: 47px; top: 64px; }
  .card--front .brand__square { margin-right: 39px; }
  .card--front .brand__name { margin-left: 14px; margin-top: -4px; }
  .card--front .brand__name .primary { font-size: 62px; letter-spacing: 1px; }
  .card--front .brand__name .secondary { font-size: 30px; letter-spacing: 0.5px; }
  .front-rule {
    position: absolute;
    left: 181px;
    top: 64px;
    width: 2px;
    height: 302px;
    background: var(--rule);
  }

  .contact {
    position: absolute;
    left: 136px;
    top: 184px;
    color: var(--ink);
  }
  .contact__row {
    display: flex;
    align-items: center;
    position: relative;
  }
  .contact__icon {
    width: 20px;
    height: 20px;
    margin-right: 61px;
    fill: var(--brand-blue);
    flex: none;
  }
  .contact__name {
    color: var(--brand-blue);
    font-size: 27px;
    line-height: 34px;
  }
  .contact__licence {
    margin-left: 81px;
    font-size: 19px;
    line-height: 26px;
    margin-bottom: 22px;
  }
  .contact__row--detail {
    font-size: 19px;
    line-height: 28px;
  }
  .contact__row--detail .contact__icon { width: 18px; height: 18px; margin-right: 63px; }

  /* back */
  .card--back .brand { left: 170px; top: 152px; }
  .card--back .brand__square { width: 120px; height: 93px; margin-right: 20px; }
  .card--back .brand__rule { height: 123px; }
  .card--back .brand__name { margin-left: 16px; margin-top: 4px; }
  .card--back .brand__name .primary { font-size: 70px; letter-spacing: 1px; }
  .card--back .brand__name .secondary { font-size: 34px; letter-spacing: 0.5px; }
</style>
</head>
<body>

<section class="card card--front" aria-label="Card front">
  <div class="skyline-backdrop" role="img" aria-label="Faint downtown skyline backdrop"></div>

  <div class="brand">
    <div class="brand__square" aria-hidden="true"></div>
  </div>
  <div class="front-rule" aria-hidden="true"></div>
  <div class="brand" style="left:195px;top:60px;">
    <p class="brand__name" style="margin-left:0;">
      <span class="primary" style="font-size:62px;">Tarvo</span>
      <span class="secondary" style="font-size:30px;">Commercial</span>
    </p>
  </div>

  <div class="contact">
    <div class="contact__row">
      <svg class="contact__icon" viewBox="0 0 20 20" aria-hidden="true">
        <circle cx="10" cy="6" r="5"/>
        <path d="M1 20c0-6 4-8 9-8s9 2 9 8z"/>
      </svg>
      <p class="contact__name">Colin Farrow</p>
    </div>
    <p class="contact__licence">lic# 07281549</p>

    <div class="contact__row contact__row--detail">
      <svg class="contact__icon" viewBox="0 0 20 20" aria-hidden="true">
        <path d="M4 1l4 4-2 3c1 3 3 5 6 6l3-2 4 4-3 3C9 19 1 11 1 4z"/>
      </svg>
      <p>415.555.0172</p>
    </div>
    <div class="contact__row contact__row--detail">
      <svg class="contact__icon" viewBox="0 0 20 20" aria-hidden="true">
        <path d="M1 4h18v12H1z M1 4l9 7 9-7" fill="none" stroke="#5d7196" stroke-width="2"/>
      </svg>
      <p>colin@tarvo-commercial.example</p>
    </div>
    <div class="contact__row contact__row--detail">
      <svg class="contact__icon" viewBox="0 0 20 20" aria-hidden="true">
        <circle cx="10" cy="10" r="9"/>
        <path d="M5 6c2 0 3 1 3 3s-2 2-2 4M12 3c0 2 2 2 3 3M12 17c0-2 1-3 3-3" fill="none" stroke="#eaeaed" stroke-width="1.5"/>
      </svg>
      <p>tarvo-commercial.example</p>
    </div>
  </div>
</section>

<section class="card card--back" aria-label="Card back">
  <div class="brand">
    <div class="brand__square" aria-hidden="true"></div>
    <div class="brand__rule" aria-hidden="true"></div>
    <p class="brand__name">
      <span class="primary">Tarvo</span>
      <span class="secondary">Commercial</span>
    </p>
  </div>
</section>

</body>
</html>
```